Maplebrook Cremations Postcard

Postcards to explain our services. Modern yet professional remembering this is about people's loved one's. Use Poppins font and Century Gothic.

Target Market(s)

People who's loved ones are going to pass away.

Font styles to use
Sans Serif

Colors
33a6d7

Requirements
Must have
• Logo, website, all the information from the attachments.

```html
<!DOCTYPE html>
<html lang="en">
<head>
<meta charset="utf-8">
<title>Maplebrook Cremations Postcard</title>
<link href="https://fonts.googleapis.com/css2?family=Poppins:wght@300;400;500;600;700&display=swap" rel="stylesheet">
<style>
  :root{
    --brand-blue:#1fa3dd;
    --brand-blue-deep:#0b8fd4;
    --brand-orange:#f5780a;
    --sea-light:#22b6ea;
    --sea-deep:#0f86d6;
    --sunset-gold:#c99a3c;
    --sunset-sand:#8a6a48;
    --white:#ffffff;
    --page:#ecebe8;
  }
  *{box-sizing:border-box;margin:0;padding:0}
  html,body{width:1200px;height:1148px;overflow:hidden}
  body{background:var(--page);font-family:"Poppins",sans-serif;position:relative}
  .card{position:absolute;left:210px;width:780px;height:520px;overflow:hidden;box-shadow:0 4px 14px rgba(0,0,0,.12)}
  .card--front{top:36px;background:var(--white)}
  .card--back{top:592px;background:linear-gradient(180deg,var(--sea-light) 0%,var(--brand-blue) 45%,var(--sea-deep) 100%);color:var(--white)}
  .shapes{position:absolute;inset:0}
  .brand{position:absolute;display:flex;align-items:center;gap:12px}
  .brand__dot{width:58px;height:58px;border-radius:50%;background:var(--brand-orange);flex:none}
  .brand__name{font-weight:600;color:var(--brand-blue);font-size:24px;line-height:1.05;letter-spacing:2px;text-transform:uppercase}
  .brand--front{left:40px;top:30px}
  .tab-text{position:absolute;left:390px;width:360px;top:55px;text-align:center;color:var(--white);font-weight:700;font-size:29px;letter-spacing:.3px}
  .hero{position:absolute;left:31px;top:110px;width:719px;height:308px;border-top-right-radius:18px;
    background:linear-gradient(180deg,var(--sunset-gold) 0%,var(--sunset-sand) 100%)}
  .hero__copy{position:absolute;left:0;right:0;top:88px;text-align:center;color:var(--white)}
  .hero__title{font-weight:700;font-size:32px;letter-spacing:.2px;line-height:1.1}
  .hero__sub{display:inline-block;margin-top:6px;padding:2px 0;border-top:1.5px solid var(--white);border-bottom:1.5px solid var(--white);font-size:19px;font-weight:400}
  .hero__phone{margin-top:6px;font-weight:700;font-size:56px;line-height:1.1;letter-spacing:1px}
  .web{position:absolute;left:62px;top:432px;color:var(--white);font-weight:700;font-size:28px;letter-spacing:.3px}
  .social{position:absolute;left:640px;top:442px;display:flex;gap:6px}
  .social__box{width:33px;height:33px;border:3px solid var(--brand-blue);border-radius:8px}
  .sea{position:absolute;inset:0;background:radial-gradient(ellipse at 55% 70%,rgba(10,110,200,.45),transparent 60%)}
  .brand--back{left:40px;top:50px;flex-direction:column;gap:8px;align-items:center}
  .brand--back .brand__dot{background:var(--white);width:70px;height:70px}
  .brand--back .brand__name{color:var(--white);font-size:22px;text-align:center}
  .contact{position:absolute;right:44px;top:95px;text-align:right}
  .contact__phone{font-weight:700;font-size:44px;line-height:1;letter-spacing:1px}
  .contact__email{font-size:18px;font-weight:400;margin-top:4px}
  .services__title{position:absolute;left:39px;top:222px;font-weight:700;font-size:23px}
  .services{position:absolute;list-style:none;font-size:16px;font-weight:300;line-height:1.2}
  .services--left{left:39px;top:272px}
  .services--right{left:420px;top:270px;width:330px}
  .services li{display:flex;gap:10px;margin-bottom:12px}
  .services--right li{margin-bottom:10px}
  .tick{flex:none;width:20px;height:18px;margin-top:1px}
</style>
</head>
<body>
  <section class="card card--front">
    <svg class="shapes" viewBox="0 0 780 520" aria-hidden="true">
      <path d="M350 112 C385 112 372 37 420 37 H732 Q750 37 750 55 V112 Z" fill="var(--brand-blue)"/>
      <path d="M31 418 H640 C600 418 612 490 560 490 H51 Q31 490 31 470 Z" fill="var(--brand-orange)"/>
    </svg>
    <div class="brand brand--front">
      <span class="brand__dot"></span>
      <span class="brand__name">Maplebrook<br>Cremations</span>
    </div>
    <div class="tab-text">$695 ALL-INCLUSIVE</div>
    <div class="hero" role="img" aria-label="Photo of a golden sunset over the ocean with waves on the beach">
      <div class="hero__copy">
        <div class="hero__title">ONLINE ARRANGEMENT CENTER</div>
        <div class="hero__sub">Hand Delivery of Cremated Remains Miami-Dade County</div>
        <div class="hero__phone">(305) 555-0147</div>
      </div>
    </div>
    <div class="web">MAPLEBROOKCREMATIONS.COM</div>
    <div class="social" aria-hidden="true">
      <span class="social__box"></span>
      <span class="social__box"></span>
    </div>
  </section>

  <section class="card card--back">
    <div class="sea" role="img" aria-label="Soft underwater photo of a seashell on blue sand"></div>
    <div class="brand brand--back">
      <span class="brand__dot"></span>
      <span class="brand__name">Maplebrook<br>Cremations</span>
    </div>
    <div class="contact">
      <div class="contact__phone">(305) 555-0147</div>
      <div class="contact__email">HELLO@MAPLEBROOKCREMATIONS.COM</div>
    </div>
    <h2 class="services__title">OUR SERVICE</h2>
    <ul class="services services--left">
      <li><svg class="tick" viewBox="0 0 20 18"><path d="M3 9 L8 14 L17 4" fill="none" stroke="#fff" stroke-width="2.4" stroke-linecap="round" stroke-linejoin="round"/></svg>Filing Death Certificate</li>
      <li><svg class="tick" viewBox="0 0 20 18"><path d="M3 9 L8 14 L17 4" fill="none" stroke="#fff" stroke-width="2.4" stroke-linecap="round" stroke-linejoin="round"/></svg>Bringing Your Loved One into our Care</li>
      <li><svg class="tick" viewBox="0 0 20 18"><path d="M3 9 L8 14 L17 4" fill="none" stroke="#fff" stroke-width="2.4" stroke-linecap="round" stroke-linejoin="round"/></svg>Refrigeration</li>
      <li><svg class="tick" viewBox="0 0 20 18"><path d="M3 9 L8 14 L17 4" fill="none" stroke="#fff" stroke-width="2.4" stroke-linecap="round" stroke-linejoin="round"/></svg>Crematory Fee</li>
      <li><svg class="tick" viewBox="0 0 20 18"><path d="M3 9 L8 14 L17 4" fill="none" stroke="#fff" stroke-width="2.4" stroke-linecap="round" stroke-linejoin="round"/></svg>Alternative Container (Cardboard)</li>
      <li><svg class="tick" viewBox="0 0 20 18"><path d="M3 9 L8 14 L17 4" fill="none" stroke="#fff" stroke-width="2.4" stroke-linecap="round" stroke-linejoin="round"/></svg>Temporary Container (Cardboard)</li>
    </ul>
    <ul class="services services--right">
      <li><svg class="tick" viewBox="0 0 20 18"><path d="M3 9 L8 14 L17 4" fill="none" stroke="#fff" stroke-width="2.4" stroke-linecap="round" stroke-linejoin="round"/></svg>Hand Delivery of Cremated Remains Miami-Dade County</li>
      <li><svg class="tick" viewBox="0 0 20 18"><path d="M3 9 L8 14 L17 4" fill="none" stroke="#fff" stroke-width="2.4" stroke-linecap="round" stroke-linejoin="round"/></svg>Medical Examiner Cremation Approval Fee</li>
      <li><svg class="tick" viewBox="0 0 20 18"><path d="M3 9 L8 14 L17 4" fill="none" stroke="#fff" stroke-width="2.4" stroke-linecap="round" stroke-linejoin="round"/></svg>1st Copy of Death Certificate</li>
      <li><svg class="tick" viewBox="0 0 20 18"><path d="M3 9 L8 14 L17 4" fill="none" stroke="#fff" stroke-width="2.4" stroke-linecap="round" stroke-linejoin="round"/></svg>Online Guestbook</li>
    </ul>
  </section>
</body>
</html>
```